Reed & Vale NC grand opening (for BILLBOARD)

Advertising the grand opening of our cannabis/hemp shop in NC. We will sell all things hemp (flower, cartridges, disposables, edibles, creams, lotions, pet products etc...)

Requirements
Must have
• include, open starting Aug 1, but grand opening Aug 15th.
Nice to have
• Difference slogan ideas "Save some cash, buy our grass" "Find your perfect high at Reed & Vale cannabis store" "Experience Nature's Gift: Reed & Vale Cannabis Store"

```html
<!DOCTYPE html>
<html lang="en">
<head>
<meta charset="utf-8">
<title>Reed &amp; Vale Billboard</title>
<link rel="stylesheet" href="https://fonts.googleapis.com/css2?family=Outfit:wght@500;600&family=Poppins:ital,wght@1,500&display=swap">
<style>
  :root {
    --navy: #0e1236;
    --navy-deep: #0a0d2a;
    --leaf-green: #7cc242;
    --leaf-bright: #4fd23a;
    --leaf-mid: #2f8a2c;
    --leaf-dark: #123a22;
    --white: #ffffff;
  }
  * { margin: 0; padding: 0; box-sizing: border-box; }
  html, body {
    width: 1200px;
    height: 353px;
    overflow: hidden;
    background: var(--navy);
  }
  .billboard {
    position: relative;
    width: 1200px;
    height: 353px;
    overflow: hidden;
    background: linear-gradient(90deg, var(--navy-deep) 0%, var(--navy) 45%, #101a30 100%);
  }
  .leaf-photo {
    position: absolute;
    top: 0;
    right: 0;
    width: 860px;
    height: 353px;
    background:
      radial-gradient(ellipse 420px 260px at 60% 55%, rgba(79, 210, 58, 0.55), rgba(79, 210, 58, 0) 75%),
      radial-gradient(ellipse 320px 300px at 95% 35%, rgba(110, 200, 60, 0.4), rgba(110, 200, 60, 0) 75%),
      linear-gradient(90deg, rgba(14, 18, 54, 0) 0%, rgba(18, 58, 34, 0.85) 35%, var(--leaf-dark) 70%, #1a3a1c 100%);
  }
  .tagline {
    position: absolute;
    left: 57px;
    top: 9px;
    font-family: "Poppins", sans-serif;
    font-style: italic;
    font-weight: 500;
    font-size: 30px;
    letter-spacing: -0.3px;
    color: var(--white);
    white-space: nowrap;
  }
  .tagline-rule {
    position: absolute;
    left: 0;
    top: 46px;
    width: 571px;
    height: 1.5px;
    background: var(--leaf-green);
  }
  .brand-name {
    position: absolute;
    left: 54px;
    top: 134px;
    font-family: "Outfit", sans-serif;
    font-weight: 500;
    font-size: 110px;
    line-height: 1;
    letter-spacing: -2px;
    color: var(--leaf-green);
    white-space: nowrap;
  }
  .location {
    position: absolute;
    left: 194px;
    top: 256px;
    font-family: "Outfit", sans-serif;
    font-weight: 500;
    font-size: 26px;
    color: var(--white);
    white-space: nowrap;
  }
  .opening-dates {
    position: absolute;
    left: 194px;
    top: 298px;
    font-family: "Outfit", sans-serif;
    font-weight: 600;
    font-size: 22px;
    color: var(--leaf-green);
    white-space: nowrap;
  }
</style>
</head>
<body>
  <main class="billboard">
    <div class="leaf-photo" role="img" aria-label="Close-up photograph of green cannabis leaves glowing against a dark background"></div>
    <p class="tagline">Save some cash, buy our grass</p>
    <div class="tagline-rule"></div>
    <h1 class="brand-name">Reed &amp; Vale</h1>
    <p class="location">Exit 9B Maple Ridge Rd</p>
    <p class="opening-dates">Open Aug 1 · Grand Opening Aug 15</p>
  </main>
</body>
</html>
```